Promotional ads for the upcoming book, "Beneath the Copper Lantern" by KRVO Press

We would like the following ad sizes to promote the release of our new book, "Beneath the Copper Lantern", published by KRVO Press:
1) wide skyscraper (160x600)
2) large rectangle (336x200)
3) square (250x250)
4) leaderboard (728x90)
5) inline rectangle (300x250)
The ads are to be displayed on our website, https://www.krvoarchive.org/

```html
<!DOCTYPE html>
<html lang="en">
<head>
<meta charset="utf-8">
<title>Beneath the Copper Lantern – Ad Set</title>
<link rel="stylesheet" href="https://fonts.googleapis.com/css2?family=Barlow+Condensed:wght@500;600&display=swap">
<style>
  :root{
    --board:#6d7075;
    --navy:#1b3a52;
    --red:#d0202e;
    --cream-light:#f8f5ee;
    --cream-dark:#e6dcc6;
    --white:#ffffff;
    --sepia-light:#b59f78;
    --sepia-dark:#5e4d36;
  }
  *{box-sizing:border-box;margin:0;padding:0}
  html,body{width:1200px;height:1200px;overflow:hidden}
  body{background:var(--board);position:relative;font-family:"Barlow Condensed",sans-serif;text-transform:uppercase}
  .ad{position:absolute;overflow:hidden;background:linear-gradient(135deg,var(--cream-light),var(--cream-dark))}
  .ad-shape{position:absolute;inset:0;width:100%;height:100%}
  .ad-shape polygon{fill:var(--navy)}
  .abs{position:absolute}
  .kicker{color:var(--red);font-weight:600;line-height:1;white-space:nowrap}
  .title{font-weight:600;line-height:1.02;color:var(--white);white-space:nowrap}
  .title.on-cream{color:var(--navy)}
  .byline{color:var(--red);font-weight:600;line-height:1;white-space:nowrap}
  .subtitle{color:var(--red);font-weight:500;line-height:1.15}
  .book{position:absolute;background:linear-gradient(170deg,var(--sepia-light) 0%,#8f7955 55%,var(--sepia-dark) 100%);
        box-shadow:6px 0 0 #f1efea,7px 0 0 #cfcac0,10px 8px 14px rgba(0,0,0,.3)}
  .publisher{position:absolute;text-align:center;color:var(--navy)}
  .publisher .by{display:block;color:var(--red);text-transform:none;font-weight:600;text-align:right}
  .publisher .mark{display:flex;align-items:center;justify-content:center;gap:5px;font-weight:500;line-height:1;white-space:nowrap}
  .publisher .mark i{display:block;background:var(--navy);flex:none}
  .publisher .org{display:block;text-transform:none;font-weight:500;line-height:1.1;white-space:nowrap}

  .leaderboard{left:100px;top:138px;width:966px;height:119px}
  .skyscraper{left:100px;top:290px;width:212px;height:796px}
  .large-rect{left:346px;top:290px;width:446px;height:265px}
  .square{left:346px;top:622px;width:332px;height:332px}
  .inline-rect{left:702px;top:622px;width:398px;height:332px}
</style>
</head>
<body>

<!-- Leaderboard -->
<section class="ad leaderboard" aria-label="Leaderboard ad">
  <svg class="ad-shape" viewBox="0 0 966 119" preserveAspectRatio="none"><polygon points="0,0 462,0 368,119 0,119"/></svg>
  <p class="abs kicker" style="left:58px;top:24px;font-size:24px">New Release</p>
  <h2 class="abs title" style="left:58px;top:52px;font-size:26px">Beneath the Copper Lantern</h2>
  <p class="abs byline" style="left:58px;top:85px;font-size:13px">By Walter R. Hale</p>
  <div class="book" style="left:380px;top:6px;width:62px;height:106px" role="img" aria-label="Book cover with sepia group photograph"></div>
  <p class="abs subtitle" style="left:466px;top:43px;font-size:20px;width:300px">Civilian scouts and lamp keepers of the Knox River Valley, 1851-1903</p>
  <div class="publisher" style="left:770px;top:40px;width:160px">
    <span class="by" style="font-size:9px">published by</span>
    <span class="mark" style="font-size:28px"><i style="width:16px;height:16px"></i>KRVO Press</span>
    <span class="org" style="font-size:10px">Knox River Valley Archive</span>
  </div>
</section>

<!-- Wide skyscraper -->
<section class="ad skyscraper" aria-label="Wide skyscraper ad">
  <svg class="ad-shape" viewBox="0 0 212 796" preserveAspectRatio="none"><polygon points="0,0 212,0 212,500 0,306"/></svg>
  <p class="abs kicker" style="left:23px;top:92px;font-size:33px">New Release</p>
  <h2 class="abs title" style="left:23px;top:134px;font-size:36px">Beneath the<br>Copper<br>Lantern</h2>
  <p class="abs byline" style="left:23px;top:272px;font-size:14px">By Walter R. Hale</p>
  <div class="book" style="left:14px;top:320px;width:176px;height:314px" role="img" aria-label="Book cover with sepia group photograph"></div>
  <div class="publisher" style="left:8px;top:660px;width:196px">
    <span class="by" style="font-size:11px">published by</span>
    <span class="mark" style="font-size:34px"><i style="width:20px;height:20px"></i>KRVO Press</span>
    <span class="org" style="font-size:13px">Knox River Valley Archive</span>
  </div>
</section>

<!-- Large rectangle -->
<section class="ad large-rect" aria-label="Large rectangle ad">
  <svg class="ad-shape" viewBox="0 0 446 265" preserveAspectRatio="none"><polygon points="0,0 278,0 174,265 0,265"/></svg>
  <p class="abs kicker" style="left:27px;top:56px;font-size:27px">New Release</p>
  <h2 class="abs title" style="left:27px;top:90px;font-size:30px">Beneath the<br>Copper<br>Lantern</h2>
  <p class="abs byline" style="left:27px;top:208px;font-size:13px">By Walter R. Hale</p>
  <div class="book" style="left:180px;top:12px;width:138px;height:248px" role="img" aria-label="Book cover with sepia group photograph"></div>
  <p class="abs subtitle" style="left:333px;top:130px;font-size:12px;width:100px">Civilian scouts and lamp keepers of the Knox River Valley, 1851-1903</p>
  <div class="publisher" style="left:330px;top:205px;width:104px">
    <span class="by" style="font-size:6px">published by</span>
    <span class="mark" style="font-size:19px"><i style="width:10px;height:10px"></i>KRVO Press</span>
    <span class="org" style="font-size:7px">Knox River Valley Archive</span>
  </div>
</section>

<!-- Square -->
<section class="ad square" aria-label="Square ad">
  <svg class="ad-shape" viewBox="0 0 332 332" preserveAspectRatio="none"><polygon points="202,0 332,0 332,332 122,332"/></svg>
  <p class="abs kicker" style="left:21px;top:80px;font-size:22px">New Release</p>
  <h2 class="abs title on-cream" style="left:21px;top:110px;font-size:25px">Beneath the<br>Copper<br>Lantern</h2>
  <p class="abs byline" style="left:21px;top:214px;font-size:12px">By Walter R. Hale</p>
  <div class="book" style="left:156px;top:38px;width:146px;height:272px" role="img" aria-label="Book cover with sepia group photograph"></div>
  <div class="publisher" style="left:16px;top:250px;width:110px">
    <span class="by" style="font-size:6px">published by</span>
    <span class="mark" style="font-size:19px"><i style="width:10px;height:10px"></i>KRVO Press</span>
    <span class="org" style="font-size:7px">Knox River Valley Archive</span>
  </div>
</section>

<!-- Inline rectangle -->
<section class="ad inline-rect" aria-label="Inline rectangle ad">
  <svg class="ad-shape" viewBox="0 0 398 332" preserveAspectRatio="none"><polygon points="246,0 398,0 398,332 147,332"/></svg>
  <p class="abs kicker" style="left:29px;top:68px;font-size:22px">New Release</p>
  <h2 class="abs title on-cream" style="left:29px;top:98px;font-size:26px">Beneath the<br>Copper<br>Lantern</h2>
  <p class="abs byline" style="left:29px;top:202px;font-size:12px">By Walter R. Hale</p>
  <div class="book" style="left:170px;top:18px;width:162px;height:298px" role="img" aria-label="Book cover with sepia group photograph"></div>
  <div class="publisher" style="left:24px;top:238px;width:110px">
    <span class="by" style="font-size:6px">published by</span>
    <span class="mark" style="font-size:19px"><i style="width:10px;height:10px"></i>KRVO Press</span>
    <span class="org" style="font-size:7px">Knox River Valley Archive</span>
  </div>
</section>

</body>
</html>
```